Letterhead for sustainable Last Mile Logistics needed

Dear all,

we are looking for a powerful design for our letterhead. We are a Berlin-based (Germany) logistics company which delivers parcel on the last mile in a sustainable way. Design should communicate: sustainability, integrity, one family, performance-focused, passionate for excellence and customer experience. Please find company logo attached.

Looking forward for

```html
<!DOCTYPE html>
<html lang="en">
<head>
<meta charset="utf-8">
<title>Fernway Logistics – Letterhead</title>
<link rel="stylesheet" href="https://fonts.googleapis.com/css2?family=Lato:wght@400;700&family=Marck+Script&display=swap">
<style>
  :root {
    --forest: #169a45;
    --lime: #a9c915;
    --ink: #3a3a3a;
    --ink-dark: #1f1f1f;
    --paper: #f8f7f8;
    --backdrop: #e6e6e4;
  }
  * { box-sizing: border-box; margin: 0; padding: 0; }
  html, body {
    width: 1200px; height: 1111px; overflow: hidden;
    background: var(--backdrop);
  }
  .letterhead {
    position: absolute; left: 170px; top: 0;
    width: 860px; height: 1111px;
    background: var(--paper);
    font-family: "Lato", sans-serif;
    color: var(--ink);
    overflow: hidden;
  }
  .brand { position: absolute; left: 66px; top: 66px; display: flex; align-items: center; gap: 14px; }
  .brand-mark { width: 50px; height: 50px; border-radius: 50%; background: var(--forest); flex: none; }
  .brand-name {
    font-family: "Lato", sans-serif; font-weight: 700;
    font-size: 30px; line-height: 1; color: var(--forest);
  }
  .brand-tagline {
    font-family: "Lato", sans-serif; font-weight: 400; font-size: 13px;
    letter-spacing: 0.5px; color: var(--ink); margin-top: 6px;
  }
  .contact {
    position: absolute; left: 598px; top: 46px;
    border-left: 1.5px solid var(--forest);
    padding-left: 11px;
    font-style: normal;
    font-size: 14px; line-height: 17.5px; color: var(--ink-dark);
  }
  .contact-address { margin-bottom: 5px; }
  .contact-row { display: flex; align-items: center; gap: 9px; }
  .contact-row svg { width: 11px; height: 11px; fill: var(--forest); flex: none; }
  .letter {
    position: absolute; left: 66px; top: 246px; width: 727px;
    font-size: 15.4px; line-height: 17px; letter-spacing: 0.25px;
  }
  .letter p { margin-bottom: 17px; }
  .body-text { text-align: justify; }
  .salutation { font-weight: 700; font-size: 18.5px; margin: 28px 0 22px; }
  .closing { margin-top: 44px; }
  .signature {
    font-family: "Marck Script", cursive; font-size: 38px; line-height: 1;
    color: var(--ink-dark); letter-spacing: 0; margin-top: 24px;
  }
  .footer-rule { position: absolute; left: 0; right: 0; bottom: 66px; height: 5px; background: var(--forest); }
  .footer-band { position: absolute; left: 0; right: 0; bottom: 0; height: 58px; background: var(--lime); }
</style>
</head>
<body>
  <main class="letterhead">
    <header>
      <div class="brand">
        <span class="brand-mark"></span>
        <div>
          <div class="brand-name">Fernway Logistics</div>
          <div class="brand-tagline">Parcels delivered the green way</div>
        </div>
      </div>
      <address class="contact">
        <div class="contact-address">2740 Linden Row, Ste<br>220, Marlow, TX 75309</div>
        <div class="contact-row">
          <svg viewBox="0 0 12 12"><path d="M1 4c0-2 2-3 5-3s5 1 5 3l-2 1-1-1.5H4L3 5zM3 6h6l1 5H2z"/></svg>
          (555) 318-2746
        </div>
        <div class="contact-row">
          <svg viewBox="0 0 12 12"><path d="M0 2h12v1L6 7 0 3zM0 4.5l6 4 6-4V10H0z"/></svg>
          hello@fernway-mail.com
        </div>
        <div class="contact-row">
          <svg viewBox="0 0 12 12"><circle cx="6" cy="6" r="5.5"/></svg>
          www.fernway-route.com
        </div>
      </address>
    </header>

    <section class="letter">
      <p>Feb-03-2022</p>
      <p>Mr, Daniel Reyes<br>President</p>
      <p>Harbor Crest Group<br>123 Street Name, Suite# 10<br>City, State, 120023</p>
      <p class="salutation">Dear Mr, Daniel</p>
      <p class="body-text">Lorem ipsum dolor sit amet, consectetur adipisicing elit, sed do eiusmod tempor incididunt ut labore et dolore magna aliqua. Ut enim ad minim veniam, quis nostrud exercitation ullamco laboris nisi ut aliquip ex ea commodo consequat. Duis aute irure dolor in reprehenderit in voluptate velit esse cillum dolore eu fugiat nulla pariatur.</p>
      <p class="body-text">Lorem ipsum dolor sit amet, consectetur adipisicing elit, sed do eiusmod tempor incididunt ut labore et dolore magna aliqua. Ut enim ad minim veniam, quis nostrud exercitation ullamco laboris nisi ut aliquip ex ea commodo consequat. Duis aute irure dolor in reprehenderit in voluptate velit esse cillum dolore eu fugiat nulla pariatur.</p>
      <p class="body-text">Lorem ipsum dolor sit amet, consectetur adipisicing elit, sed do eiusmod tempor incididunt ut labore et dolore magna aliqua. Ut enim ad minim veniam, quis nostrud exercitation ullamco laboris nisi ut aliquip ex ea commodo consequat.</p>
      <p class="body-text">Excepteur sint occaecat cupidatat non proident, sunt in culpa qui officia deserunt mollit anim id est laborum. re et dolore magnam aliquam quaerat voluptatem.</p>
      <p class="closing">Regards</p>
      <p class="signature">Owen Hartley</p>
    </section>

    <footer aria-hidden="true">
      <div class="footer-rule"></div>
      <div class="footer-band"></div>
    </footer>
  </main>
</body>
</html>
```